依頼概要
■依頼目的/概要
電子書籍を出版いたしますので、表紙デザインをお願いいたします。

-------------
■本のタイトル
灯火(ともしび)

【サブタイトル】
~静かな朝を迎える言葉の書~
※あとから修正依頼あり

<著者>
柏木遥斗

<おまけ特典>
シベリア晴郎vs櫻庭露樹 秘密の対談動画

---------------------------
納品は、
2,560×1,600ピクセルのJPEGと元データをお願い致したく。

----著者プロフィール ご参考まで---------
《柏木遥斗》
青森県三沢市生まれ
幼少期の極貧生活と虐待により、小学三年生9歳から朝刊夕刊の新聞配達や集金をこなしながら、2つの不労所得を得るビジネスプランを完成させる。小学生時代に稼いだ金額は一千万円。24歳で起業後、フランチャイズの店舗経営を始め10店舗まで右肩上がりで経営を成功させたのち売却。追って、自由が丘と溝の口に、水晶天然石の店舗KOVUSをオープン。

現在は複数の会社で事業展開の他、各所の著名大企業からヘッドハンティングされ社外取締役などを務めながら、世界中の富豪層からも愛され何かと声をかけられる摩訶不思議な強運の持ち主、人呼んで開運マスター。

「アホと素直と行動力、プラス笑顔」を提唱し、トイレ掃除や全捨離の実践者でもある。
売れっ子芸人並みの秀逸なギャグセンスに、少年のような真っ直ぐでピュアな心と、ゴロスケのような豪快さを併せ持つ人柄に惹きつけられるファンも多く、当たり過ぎる超適当なタロット占い、恋愛や仕事、人間関係などに悩む方の人生相談会なども好評を得ている。
いまや、全国各地のみならず世界各所から、心のあり方や開運に特化した講演を依頼される超人気講師。

オンラインサロンを開設しコミュニティは大盛況で運営中。柏木の生き様や実践法、表に出せない極秘情報はもちろん、登場する超個性的な師匠や偉人たちに魅了され、世界中から人気を集めている。
2019年夏に開設したYoutubeチャンネルもすでに16万人の登録者を超えるなど大ブレイク中。

著書に、自らが支援している子供たちを描いた『僕らは丘の上でいつも笑っている仲間たち。草原の学び舎「草原の仲間たち」の物語』、トイレ掃除と開運についての名書『台所の精霊が教えた内緒の招福術 福鍋の定理』、電子書籍『福鍋のこころえ』、『7つを減らせば毎日かるくなる!総片付』、リバーサイド出版社『暮らしの巡りが整うコツを集めてみた』、『財布が喜ぶありとあらゆる習慣を調べてみた』など多数。
--------------------------
■デザイン要望

シンプル イズ ベスト。白バックに黒字の明朝体。
上品で視認性の高いもの、しかし機能的になりすぎず余白美を醸しているもの。

イメージ画像①、②の丸枠に、著者画像を組み込んでいただきたいです。
(※下記、添付ファイルをご参照くださいませ)

ーーーーご参考までーー----------------
■デザインイメージのヒントとなる『あとがき』の抜粋の一部を、下記に掲載します。

(あとがき より)
本書を通じて、宇宙法則、風水、タイムマネジメントといった多岐にわたる分野の智慧と、様々な体験と深い教養に基づいた森羅万象に精通するモルダ冬彦先生の貴重なお話の数々が散りばめられています。先生が立命するきっかけとなった出逢いや回想録にも触れ、運とは何か、ということや、運を強くする方法について語っていただきました。

歴史を振り返ってみた時に、かつての我が国、幕末の日本にも、今現在の僕たちが体験しているような混沌の時代がありました。青天の霹靂のような出来事が多発し、情報が錯綜する中で、これまでの常識や価値観は見事に崩れ落ちています。パラダイムシフトになぞらえられる、令和の今のこの世にご縁があって集まった僕たちには、時代を超え、何か大切な命題を叩きつけられているように思います。

あえてこの時代に生まれた私たちの魂の欲するところは何なのか。人生の使命とは?

冬彦先生は、そんな問いに挑戦し、各々の人生に挑戦する僕たち現代人に、いつもたくさんのヒントを提示してくださいます。今回は幕末に生きたスピリチュアル的思想の先駆者、杉村東巌先生の教えを引用し、魂の成長錬磨のよりシンプルかつ具体的な方法をもご指南いただけました。(以上 一部抜粋)

※その他イラストや写真等素材を使用される場合には、商用利用可の素材をお願いします。

■その他、デザインを考えるのに必要な情報などありましたら、
お答えしますので、遠慮なくお尋ねくださいませ。

よろしくお願い申し上げます。
たくさんのご応募誠にありがとうございました。
皆様の作品を大切に拝見し、ご尽力に感謝の気持ちでいっぱいでございます。

著者のもと鋭意選定をすすめておりますので、今しばらくお待ちいただけますと幸いに存じます。

ご高配のほどよろしくお願い申し上げます。

デザイン要望にもとづき、参考文より汲み取って頂いた
世界観が表現されていて、とても素晴らしい作品です。

著者が一番気に入ったそうなので
こちらを選定させていただきました。

この度は貴重なお時間と労力をお掛けくださり
素晴らしい作品をご応募いただきまして
本当にどうもありがとうございました。

どれも逸品で大変迷いましたが
今回はこちらに決めさせていただきました。

せっかくご応募いただきましたのに
選定できない方々、
誠に申し訳ございません。

今後ともご縁がございましたら
次回もどうぞよろしくお願い致します!

皆様のますますのご活躍を心より祈念致しております。

本当にどうもありがとうございました。

```html
<!DOCTYPE html>
<html lang="ja">
<head>
<meta charset="utf-8">
<title>灯火 表紙</title>
<link rel="stylesheet" href="https://fonts.googleapis.com/css2?family=Noto+Serif+JP:wght@400;600;700;900&family=Shippori+Mincho+B1:wght@500;700;800&display=swap">
<style>
  :root {
    --paper: #ffffff;
    --ink: #111111;
    --ink-soft: #3a3a3a;
    --vs-grey: #9a9a9a;
    --band-dark: #4a4a4a;
    --band-light: rgba(255,255,255,0);
    --portrait-top: #e9eaec;
    --portrait-bottom: #2b2e36;
  }
  html, body {
    margin: 0;
    padding: 0;
    overflow: hidden;
    background: var(--paper);
  }
  .cover {
    position: relative;
    width: 750px;
    height: 1200px;
    overflow: hidden;
    background: var(--paper);
    color: var(--ink);
    font-family: "Shippori Mincho B1", "Noto Serif JP", serif;
  }
  .title-char {
    position: absolute;
    margin: 0;
    font-family: "Shippori Mincho B1", serif;
    font-weight: 500;
    line-height: 1;
    color: var(--ink);
  }
  .title-char--first { left: 30px; top: 10px; font-size: 300px; }
  .title-char--second { left: 150px; top: 335px; font-size: 320px; }
  .title-rules { position: absolute; left: 0; top: 0; }
  .title-ruby {
    position: absolute;
    left: 292px;
    top: 306px;
    font-size: 18px;
    font-weight: 700;
    letter-spacing: 1px;
  }
  .subtitle {
    position: absolute;
    top: 122px;
    font-family: "Noto Serif JP", serif;
    font-size: 32px;
    font-weight: 600;
    writing-mode: vertical-rl;
    letter-spacing: 4px;
    margin: 0;
  }
  .subtitle--line1 { left: 570px; }
  .subtitle--line2 { left: 505px; }
  .portrait {
    position: absolute;
    left: 425px;
    top: 820px;
    width: 325px;
    height: 380px;
    background: linear-gradient(180deg, var(--portrait-top) 0%, #bfc2c7 40%, var(--portrait-bottom) 100%);
  }
  .author-name {
    position: absolute;
    left: 38px;
    top: 888px;
    margin: 0;
    font-family: "Noto Serif JP", serif;
    font-weight: 900;
    font-size: 80px;
    letter-spacing: 4px;
    line-height: 1;
  }
  .bonus-band {
    position: absolute;
    left: 0;
    top: 1025px;
    width: 430px;
    height: 56px;
    background: linear-gradient(90deg, var(--band-dark) 0%, #8a8a8a 45%, var(--band-light) 100%);
  }
  .bonus-guest, .bonus-host {
    position: absolute;
    top: 1038px;
    font-family: "Noto Serif JP", serif;
    font-weight: 600;
    font-size: 26px;
    line-height: 1.1;
  }
  .bonus-guest { left: 34px; color: var(--paper); }
  .bonus-host { left: 290px; color: var(--ink); }
  .bonus-vs {
    position: absolute;
    left: 205px;
    top: 1012px;
    font-family: "Noto Serif JP", serif;
    font-size: 64px;
    font-weight: 400;
    color: var(--vs-grey);
    line-height: 1;
  }
  .bonus-label {
    position: absolute;
    left: 38px;
    top: 1098px;
    width: 334px;
    height: 56px;
    box-sizing: border-box;
    border: 2px solid var(--ink);
    display: flex;
    align-items: center;
    justify-content: center;
    font-family: "Noto Serif JP", serif;
    font-weight: 900;
    font-size: 36px;
    letter-spacing: 2px;
  }
  .bonus-label .small { font-size: 24px; font-weight: 700; }
</style>
</head>
<body>
<main class="cover">
  <h1 class="title-char title-char--first">灯</h1>
  <span class="title-char title-char--second" aria-hidden="false">火</span>
  <svg class="title-rules" width="750" height="1200" aria-hidden="true">
    <line x1="212" y1="240" x2="212" y2="600" stroke="var(--ink)" stroke-width="3"/>
    <line x1="215" y1="676" x2="750" y2="676" stroke="var(--ink)" stroke-width="4"/>
  </svg>
  <span class="title-ruby">【ともしび】</span>

  <p class="subtitle subtitle--line1">静かな朝を</p>
  <p class="subtitle subtitle--line2">迎える　言葉の書</p>

  <div class="portrait" role="img" aria-label="著者 柏木遥斗の上半身写真（スーツ姿）"></div>
  <h2 class="author-name">柏木 遥斗</h2>

  <div class="bonus-band"></div>
  <span class="bonus-guest">モルダ 冬彦</span>
  <span class="bonus-vs">VS</span>
  <span class="bonus-host">柏木 遥斗</span>
  <div class="bonus-label">秘密<span class="small">の</span>対談動画<span class="small">つき</span></div>
</main>
</body>
</html>
```